Join Wait / Reservations Handout

This is a handout for guests with information about the ability to join our
waitlist and/or make reservations. It will be handed out to any guest that ends up waiting on our waitlist to be seated. It will describe how our waitlist and reservations system works. It is informational for them to download our mobile app.

It was forcing me to move the look and feel sliders. Please refer to our branding guide for look and feel.

Industry/Entity Type

Hospitality

Contact Information for Business Card

One of the attached documents give a very generic layout of the information we need on this card. This layout is more for where we wanted the information placed and has nothing to do with the design aspects of the piece. Please use your imagination. Any of the 5 colors in the branding guide can be used anywhere. The pineapple design can be used anywhere in any color combination.

If you require any other files please let me know. Thanks

Other font styles liked:
• Please see attached branding guide

Requirements
Must have
• The only color requirement is that the logo be the blue with teal lettering...This has to match our app store logo.

```html
<!DOCTYPE html>
<html lang="en">
<head>
<meta charset="utf-8">
<title>Join the Wait / Reservations Handout</title>
<link href="https://fonts.googleapis.com/css2?family=Noto+Serif+Display:wght@400&family=Tinos&display=swap" rel="stylesheet">
<style>
  :root {
    --teal: #5fa9ad;
    --navy: #0f2a45;
    --logo-navy: #06263d;
    --logo-teal: #6cb3b5;
    --ink: #111111;
    --paper: #ffffff;
    --spine: #e3e3e3;
    --backdrop: #f1f1ef;
    --display: "Noto Serif Display", "Times New Roman", serif;
    --body: "Tinos", "Times New Roman", serif;
  }
  * { box-sizing: border-box; margin: 0; padding: 0; }
  html, body { width: 1200px; height: 840px; overflow: hidden; }
  body { background: var(--backdrop); position: relative; }

  .handout {
    position: absolute; left: 28px; top: 10px;
    width: 1144px; height: 820px;
  }
  .panel {
    position: absolute; top: 0; height: 820px;
    background: var(--teal);
  }
  .panel--front { left: 0; width: 492px; }
  .panel--info { left: 646px; width: 498px; }
  .spine {
    position: absolute; left: 492px; top: 0;
    width: 154px; height: 820px; background: var(--spine);
  }
  .card {
    position: absolute; background: var(--paper); text-align: center;
  }
  .panel--front .card { left: 66px; top: 56px; width: 358px; height: 706px; }
  .panel--info .card { left: 60px; top: 49px; width: 380px; height: 722px; }

  /* Front card */
  .save-title {
    position: absolute; left: 0; right: 0; top: 92px;
    font-family: var(--display); font-size: 46px; line-height: 54px;
    color: var(--ink); letter-spacing: 0.5px;
  }
  .save-sub {
    position: absolute; left: 0; right: 0; top: 211px;
    font-family: var(--body); font-size: 21px; color: var(--ink);
  }
  .brand-mark {
    position: absolute; left: 50px; top: 352px; width: 265px; height: 265px;
    background: var(--logo-navy);
    display: flex; align-items: center; justify-content: center;
  }
  .brand-name {
    font-family: var(--display); font-size: 30px; line-height: 38px;
    color: var(--logo-teal); letter-spacing: 2px;
  }
  .app-search {
    position: absolute; left: 0; right: 0; bottom: 0; height: 38px;
    border-top: 1.5px solid var(--ink);
    font-family: var(--body); font-size: 20px; line-height: 34px;
    color: var(--ink);
  }

  /* Info card */
  .info-heading {
    position: absolute; left: 0; right: 0;
    font-family: var(--display); font-size: 39px; line-height: 48px;
    color: var(--navy);
  }
  .info-note {
    position: absolute; left: 0; right: 0;
    font-family: var(--body); font-size: 21px; line-height: 30px;
    color: var(--ink); white-space: nowrap;
  }
  .info-note--small { font-size: 17px; }
  .rule {
    position: absolute; left: 11px; width: 359px; height: 0;
    border-top: 1.5px solid var(--ink);
  }
</style>
</head>
<body>
  <main class="handout">
    <section class="panel panel--front" role="img" aria-label="Teal geometric diamond pattern border">
      <div class="card">
        <h1 class="save-title">SAVE THE<br>WAIT...</h1>
        <p class="save-sub">...DOWNLOAD OUR APP</p>
        <div class="brand-mark">
          <span class="brand-name">HARBORVIEW<br>DINER</span>
        </div>
        <p class="app-search">Search “Harborview Westfield”</p>
      </div>
    </section>

    <div class="spine"></div>

    <section class="panel panel--info" role="img" aria-label="Teal geometric diamond pattern border">
      <div class="card">
        <h2 class="info-heading" style="top:6px">WHEN TO JOIN<br>THE WAIT?</h2>
        <p class="info-note" style="top:104px">*ANYTIME</p>
        <div class="rule" style="top:179px"></div>

        <h2 class="info-heading" style="top:185px">WHEN TO<br>RESERVE?</h2>
        <p class="info-note" style="top:284px; font-size:20px; letter-spacing:-0.5px">*ANYTIME /2 HOURS IN ADVANCE</p>
        <p class="info-note info-note--small" style="top:315px">EXCLUDING WEEKEND, OPEN&nbsp; - 2PM</p>
        <div class="rule" style="top:355px"></div>

        <h2 class="info-heading" style="top:364px">SUNDAY+<br>HOLIDAY BUFFETS</h2>
        <p class="info-note" style="top:463px">*COMING JUNE 2018</p>
        <div class="rule" style="top:533px"></div>

        <h2 class="info-heading" style="top:539px">LARGE<br>GROUPS</h2>
        <p class="info-note" style="top:638px">* HANDLED/CONTACTED</p>
        <p class="info-note" style="top:668px">BY CATERING MANAGER</p>
        <div class="rule" style="top:710px"></div>
      </div>
    </section>
  </main>
</body>
</html>
```